Copper Lantern - responsive bootstrap website design

Looking to build a responsive service website.

Logo has been provided.

PLEASE REVIEW ATTACHED DESIGN STYLE GUIDES & CLIENT CREATIVE BRIEF FOR OUR REQUIREMENT.

THANK YOU AND GOOD LUCK!

Industry/Entity Type

Build

```html
<!DOCTYPE html>
<html lang="en">
<head>
<meta charset="utf-8">
<title>Copper Lantern Outfitters</title>
<link rel="stylesheet" href="https://fonts.googleapis.com/css2?family=Open+Sans:wght@400;600;700&display=swap">
<style>
:root{
  --ink:#0a0a0a;
  --bar:#141414;
  --blue:#1d3f9b;
  --blue-bright:#2a6ad8;
  --paper:#f2f2f2;
  --text-light:#e8e8e8;
  --text-dark:#333;
  --muted:#777;
  --rule:#cfcfcf;
  --fb:#3b5a9a;
  --tw:#2cb8ea;
  --ig:#e7e2da;
  --pink:#ee5a7a;
}
*{box-sizing:border-box;margin:0;padding:0}
html,body{width:686px;height:1200px;overflow:hidden}
body{position:relative;background:var(--paper);font-family:"Open Sans",Arial,sans-serif;color:var(--text-dark)}
.abs{position:absolute}

.topbar{top:0;left:0;width:686px;height:24px;background:var(--bar)}
.topbar .contact{right:216px;top:6px;font-size:7.5px;font-weight:700;color:var(--blue-bright);white-space:nowrap}
.topbar .contact span{color:#fff;font-weight:400}
.topbar .search{left:476px;top:6px;width:106px;height:13px;background:#1e1e1e;border:1px solid #2a2a2a;font-size:6px;color:#999;padding:2px 4px}
.topbar .search svg{position:absolute;right:4px;top:3px}

.header{top:24px;left:0;width:686px;height:50px;background:var(--ink)}
.brand{left:104px;top:12px;display:flex;align-items:center;gap:6px;color:#fff;font-size:11px;font-weight:600;line-height:1.1}
.brand i{width:12px;height:12px;border-radius:50%;border:1.5px solid #fff;display:block}
.nav{left:260px;top:0;height:50px;display:flex}
.nav a{display:block;height:50px;line-height:52px;padding:0 8px;font-size:8px;color:#fff;text-decoration:none}
.nav a.active{background:var(--blue)}

.hero{top:74px;left:0;width:686px;height:233px;background:linear-gradient(180deg,#1c3d78 0%,#2c4f8a 40%,#d8dde2 75%,#e8e8e8 100%)}
.dots{left:323px;top:289px;display:flex;gap:3px}
.dots i{width:8px;height:8px;border-radius:50%;background:#fff;display:block}
.dots i.on{background:var(--blue)}

.fishing{top:307px;left:0;width:686px;height:272px;background:var(--ink)}
.section-title{font-size:8px;font-weight:700;color:var(--blue);text-transform:uppercase}
.fishing .section-title{left:0;width:686px;top:21px;text-align:center}
.area{top:39px;width:116px;height:74px}
.area .photo{width:116px;height:74px}
.area .label{position:absolute;left:0;bottom:0;width:116px;height:15px;background:rgba(0,0,0,.55);color:#fff;font-size:6px;padding:4px 6px}
.area .label i{position:absolute;right:5px;top:4px;width:7px;height:7px;border-radius:50%;background:var(--blue-bright)}

.welcome{left:104px;top:132px;width:297px}
.welcome h2{font-size:7px;font-weight:700;color:var(--blue);text-transform:uppercase;padding-bottom:6px;border-bottom:1px solid #333}
.welcome p{font-size:5.8px;line-height:12px;color:var(--text-light);margin-top:8px}
.welcome h3{font-size:6px;font-weight:700;color:#fff;margin-top:14px}
.welcome h3+p{margin-top:2px}
.welcome b{color:#fff}

.news{left:424px;top:132px;width:158px}
.news h2{font-size:7px;font-weight:700;color:var(--blue);text-transform:uppercase;padding-bottom:6px;border-bottom:1px solid #333}
.news-item{position:relative;height:59px;border-bottom:1px solid #333}
.news-item .thumb{position:absolute;left:7px;top:9px;width:43px;height:33px}
.news-item p{position:absolute;left:62px;top:6px;width:96px;font-size:5.4px;font-weight:700;line-height:12px;color:#fff}
.news-item a{position:absolute;left:62px;top:44px;font-size:5.5px;color:var(--blue)}

.blog .section-title{left:104px;top:590px}
.arrows{left:564px;top:590px;font-size:9px;color:#333;letter-spacing:4px}
.post{top:611px;width:156px}
.post .photo{width:156px;height:82px}
.post h4{font-size:5.8px;font-weight:700;line-height:12px;margin-top:9px;color:#222}
.post p{font-size:5.5px;line-height:12px;color:#555;margin-top:12px}
.post .rule{height:1px;background:var(--rule);margin-top:8px}
.post .actions{display:flex;align-items:center;gap:3px;margin-top:9px;font-size:5px;color:#333}
.btn{display:inline-block;background:var(--blue);color:#fff;font-size:6px;font-weight:700;padding:4px 7px;margin-right:6px}
.post .actions .dot{width:8px;height:8px;border-radius:50%;display:inline-block}

.gallery-title{top:833px}
.video{left:104px;top:851px;width:262px;height:151px;background:linear-gradient(180deg,#1b6ad6 0%,#4aa1ea 50%,#6fc9c0 85%,#3fae9a 100%)}
.thumbs{left:122px;top:966px;display:flex;gap:6px}
.thumbs div{width:41px;height:26px;border:2px solid #fff;background:#6b8f9e}
.picture{left:380px;top:851px;width:201px;height:151px;background:linear-gradient(180deg,#aebacb 0%,#8c9aa8 45%,#c44d36 60%,#6a6d6a 100%)}
.chev{width:14px;height:14px;border-radius:50%;background:#fff}
.chev svg{display:block}

.social{top:1022px;left:0;width:686px;height:178px;background:var(--ink)}
.box{top:14px;width:155px;height:112px;background:#fff}
.box .band{height:36px;color:#fff;font-size:13px;font-weight:700;padding:9px 11px}
.fb .band{background:var(--fb)}
.tw .band{background:var(--tw)}
.ig .band{background:var(--ig);color:#333;height:36px}
.fb .avatar{position:absolute;left:5px;top:46px;width:31px;height:24px;background:#1b1b1b}
.fb p{position:absolute;left:46px;top:44px;width:104px;font-size:6.2px;line-height:12px;color:#888}
.fb .meta{position:absolute;left:46px;top:98px;font-size:4.5px;color:#3b5a9a}
.tw .bird{position:absolute;left:9px;top:46px;width:9px;height:7px;border-radius:50%;background:var(--tw)}
.tw p{position:absolute;left:26px;top:45px;width:124px;font-size:6.2px;line-height:11px;color:#555}
.tw p b{color:#333;font-weight:600}
.tw p a{color:var(--tw);text-decoration:none}
.tw .meta{position:absolute;left:24px;top:92px;font-size:5px;color:#666;display:flex;gap:14px}
.ig .count{position:absolute;right:16px;top:8px;font-size:5.5px;color:#333}
.ig .follow{position:absolute;right:10px;top:17px;background:var(--pink);color:#fff;font-size:5.5px;font-weight:700;padding:2px 8px;border-radius:2px}
.ig .grid{position:absolute;left:12px;top:46px;display:grid;grid-template-columns:repeat(4,28px);gap:4px 4px}
.ig .grid div{height:23px;border:1px solid #fff}

.footer-nav{left:104px;font-size:6px;color:#888}
.footer-nav span{margin:0 5px}
.copy{left:104px;font-size:5.5px;color:#666}
.follow-icons{left:531px;display:flex;gap:3px}
.follow-icons i{width:15px;height:15px;border-radius:50%;background:#555;display:block}
</style>
</head>
<body>

<div class="abs topbar">
  <div class="abs contact">Harbor Point Coastal Bay : <span>555-014-2277</span></div>
  <div class="abs search">Search
    <svg width="6" height="6" viewBox="0 0 6 6"><circle cx="2.4" cy="2.4" r="1.8" fill="none" stroke="#bbb" stroke-width=".8"/><line x1="3.7" y1="3.7" x2="5.6" y2="5.6" stroke="#bbb" stroke-width=".8"/></svg>
  </div>
</div>

<header class="abs header">
  <div class="abs brand"><i></i><div>Copper Lantern<br>Outfitters</div></div>
  <nav class="abs nav">
    <a class="active" href="#">Home Page</a>
    <a href="#">About Us</a>
    <a href="#">Guide Services</a>
    <a href="#">Merchandise</a>
    <a href="#">Video</a>
    <a href="#">Picture Gallery</a>
  </nav>
</header>

<div class="abs hero" role="img" aria-label="Two anglers on a boat holding up a large catch, numbered tournament card, open ocean behind"></div>
<div class="abs dots"><i class="on"></i><i></i><i></i><i></i></div>

<section class="abs fishing">
  <h2 class="abs section-title">Fishing Area</h2>
  <div class="abs area" style="left:104px"><div class="photo" role="img" aria-label="Boat near the shoreline under a blue sky" style="background:linear-gradient(180deg,#4f8fd0,#7fa6b8 55%,#2f5f8a)"></div><div class="label">In - Shore<i></i></div></div>
  <div class="abs area" style="left:225px"><div class="photo" role="img" aria-label="Angler casting offshore from a boat" style="background:linear-gradient(180deg,#3f6fb8,#7c9cc8 55%,#2a4f86)"></div><div class="label">Off - Shore<i></i></div></div>
  <div class="abs area" style="left:346px"><div class="photo" role="img" aria-label="Calm pond at sunset with reeds" style="background:linear-gradient(180deg,#e6dca8,#a7a35a 55%,#4e6a3a)"></div><div class="label">Pond<i></i></div></div>
  <div class="abs area" style="left:466px"><div class="photo" role="img" aria-label="Fly fishing lure resting on blue water" style="background:linear-gradient(135deg,#0f3a78,#2f7ad0 60%,#8ab8e0)"></div><div class="label">Fly - Fishing<i></i></div></div>

  <div class="abs welcome">
    <h2>Welcome to Copper Lantern Outfitters</h2>
    <p>Lowcountry's own Copper Lantern Outfitters is your ultimate destination for saltwater fishing. From fly fishing for tailing reds in a foot of water to chasing Pelagic in the Gulf Stream, here you'll find all the gear, apparel, and expert advice you'll need to make the most of your time on the water.</p>
    <h3>GUIDE SERVICES</h3>
    <p>Looking for guidance? Copper Lantern Outfitters provides professional guide services featuring the areas' best captains and crews. Regardless of your skill level or experience, we can accommodate your group to create an exhilarating and memorable fishing experience. <b>more ...</b></p>
  </div>

  <div class="abs news">
    <h2>Latest News</h2>
    <div class="news-item"><div class="thumb" role="img" aria-label="Fishing reel close-up" style="background:linear-gradient(135deg,#2a8fb0,#9fb6c0)"></div><p>Accusamus et iusto odio dignissimos ducimus qui blanditiis praesentium voluptatum</p><a>Read More</a></div>
    <div class="news-item"><div class="thumb" role="img" aria-label="Tackle gear on a dock" style="background:linear-gradient(135deg,#3a9ab8,#b9a98a)"></div><p>Accusamus et iusto odio dignissimos ducimus qui blanditiis praesentium voluptatum</p><a>Read More</a></div>
  </div>
</section>

<section class="blog">
  <h2 class="abs section-title">Blog</h2>
  <div class="abs arrows">‹ ›</div>

  <article class="abs post" style="left:104px">
    <div class="photo" role="img" aria-label="Angler holding a red snapper at sea" style="background:linear-gradient(180deg,#3f74c0,#6b95c8 45%,#d4544a 70%,#e8e8e8)"></div>
    <h4>At vero eos et accusamus et iusto odio dignissimos ducimus qui blanditiis praesentium voluptatum</h4>
    <p>Deleniti atque corrupti quos dolores et quas molestias excepturi sint occaecati cupiditate non provident, similique sunt in culpa qui officia</p>
    <div class="rule"></div>
    <div class="actions"><span class="btn">Read More</span>Share +<i class="dot" style="background:#4aa3df"></i><i class="dot" style="background:#3b5a9a"></i><i class="dot" style="background:#c8232c"></i><i class="dot" style="background:#dd4b39"></i></div>
  </article>
  <article class="abs post" style="left:265px">
    <div class="photo" role="img" aria-label="Two anglers on a flats boat by mangroves" style="background:linear-gradient(180deg,#5a8cc8,#3e7040 45%,#6f8ea4 70%,#ddd)"></div>
    <h4>At vero eos et accusamus et iusto odio dignissimos ducimus qui blanditiis praesentium voluptatum</h4>
    <p>Deleniti atque corrupti quos dolores et quas molestias excepturi sint occaecati cupiditate non provident, similique sunt in culpa qui officia</p>
    <div class="rule"></div>
    <div class="actions"><span class="btn">Read More</span>Share +<i class="dot" style="background:#4aa3df"></i><i class="dot" style="background:#3b5a9a"></i><i class="dot" style="background:#c8232c"></i><i class="dot" style="background:#dd4b39"></i></div>
  </article>
  <article class="abs post" style="left:426px">
    <div class="photo" role="img" aria-label="Angler with a catch beside mangroves" style="background:linear-gradient(180deg,#8fb4e0,#4d7a48 45%,#8a8a70 70%,#e0e0e0)"></div>
    <h4>At vero eos et accusamus et iusto odio dignissimos ducimus qui blanditiis praesentium voluptatum</h4>
    <p>Deleniti atque corrupti quos dolores et quas molestias excepturi sint occaecati cupiditate non provident, similique sunt in culpa qui officia</p>
    <div class="rule"></div>
    <div class="actions"><span class="btn">Read More</span>Share +<i class="dot" style="background:#4aa3df"></i><i class="dot" style="background:#3b5a9a"></i><i class="dot" style="background:#c8232c"></i><i class="dot" style="background:#dd4b39"></i></div>
  </article>
</section>

<section class="galleries">
  <h2 class="abs section-title gallery-title" style="left:104px">Video Gallery</h2>
  <div class="abs video" role="img" aria-label="Angler poling a skiff across turquoise flats"></div>
  <svg class="abs" style="left:114px;top:915px" width="8" height="12" viewBox="0 0 8 12"><path d="M6 1 1 6l5 5" fill="none" stroke="#fff" stroke-width="2"/></svg>
  <svg class="abs" style="left:344px;top:915px" width="8" height="12" viewBox="0 0 8 12"><path d="M2 1l5 5-5 5" fill="none" stroke="#fff" stroke-width="2"/></svg>
  <div class="abs thumbs"><div></div><div></div><div></div><div></div><div></div></div>

  <h2 class="abs section-title gallery-title" style="left:380px">Picture Gallery</h2>
  <div class="abs picture" role="img" aria-label="Angler on a boat holding a large red snapper"></div>
  <div class="abs chev" style="left:384px;top:919px"><svg width="14" height="14" viewBox="0 0 14 14"><path d="M8 4 5 7l3 3" fill="none" stroke="#222" stroke-width="1.5"/></svg></div>
  <div class="abs chev" style="left:561px;top:919px"><svg width="14" height="14" viewBox="0 0 14 14"><path d="M6 4l3 3-3 3" fill="none" stroke="#222" stroke-width="1.5"/></svg></div>
</section>

<footer class="abs social">
  <div class="abs box fb" style="left:104px">
    <div class="band">friendbook</div>
    <div class="avatar"></div>
    <p>Dana Whitfield maybe I should of stood on the white pages or two when they took this photo!<br>June 13, 2012 at 2:16am</p>
    <div class="meta">Like &nbsp;&nbsp; Unlike &nbsp;&nbsp; Comment</div>
  </div>
  <div class="abs box tw" style="left:265px">
    <div class="band">chirper</div>
    <i class="bird"></i>
    <p><b>Copper Lantern Outfitters</b><br>Online and high-tech start-ups could account for 4% <a href="#">http://cl.example/8fQ2xr</a></p>
    <div class="meta"><span>↩ Reply</span><span>⇄ Retweet</span><span>★ Favourite</span></div>
  </div>
  <div class="abs box ig" style="left:425px">
    <div class="band">Snapgram</div>
    <div class="count">12,492</div>
    <div class="follow">Followers ›</div>
    <div class="grid" role="img" aria-label="Grid of eight catch photos">
      <div style="background:#e09a5a"></div><div style="background:#8a7050"></div><div style="background:#a04a3a"></div><div style="background:#c9b78a"></div>
      <div style="background:#5a8a90"></div><div style="background:#c46a50"></div><div style="background:#7a8a70"></div><div style="background:#4a8ab0"></div>
    </div>
  </div>

  <div class="abs footer-nav" style="top:140px">Home Page<span>|</span>About Us<span>|</span>Guide Services<span>|</span>Merchandise<span>|</span>Video<span>|</span>Picture Gallery</div>
  <div class="abs copy" style="top:158px">© 2014 Compnay Name ,All Rights Reserved</div>
  <div class="abs follow-icons" style="top:143px"><i></i><i></i><i></i></div>
</footer>

</body>
</html>
```